KORVA SUPERMARKET_PRODUCT LABEL DESIGN

Professional Product Label Designs to be printed on White Gloss Labels (see below). We are looking for 2 different design variations for each label size below:
a) 4.25" x 5.5" (https://www.printquilla.example/Items/PQ812XT.htm)
b) 4" x 3.25" (https://www.printquilla.example/Items/PQ367XT.htm)

See attachment "Label Design Instructions" as well as the logo files. Our Brand colors are green and blue. The brand/logo "Korva" will be used on all label designs. Eliminate/remove and do not include the bottom part that says ...Specialty Grocery, Meat&Fish, Cosmetics, Homeware... when designing. I have also attached 8 google product images that may (or may not be) inspirational...see files R1 to R8.

Target Market(s)

We are a retail supermarket targeting primarily Africans but as well as Canadians. The design needs to be unique so it appeals to both markets...a touch of authenticity combined with modernity…simple but yet alluring, attractive and appetizing as it is to be used on food products (Dry Beans, Dry Lentils, Flour, Spices) that are packaged in clear plastic poly bags. We want to reinforce and build brand loyalty among our customers. So originality, practicality, uniqueness, professional and high resolution are essential.

Industry/Entity Type

Retail

Requirements
Must have
• See attachment detailed "Label Design Instructions".
• The design needs to be unique ...a touch of authenticity combined with modernity…simple but yet alluring, attractive and appetizing as it is to be used on food products (Dry Beans, Dry Lentils, Flour, Spices) that are packaged in clear plastic poly bags. We want to reinforce and build brand loyalty among our customers. So originality, practicality, uniqueness is essential. I have also attached 8 google product images that may (or may not be) inspirational...see files R1 to R8.
Nice to have
• See attachment "Label Design Instructions" . I have also attached 8 google product images that may (or may not be) inspirational...see files R1 to R8.
Should not have
• See attachment "Label Design Instructions"

```html
<!DOCTYPE html>
<html lang="en">
<head>
<meta charset="utf-8">
<title>Korva Self-Raising Flour Labels</title>
<link rel="stylesheet" href="https://fonts.googleapis.com/css2?family=Cinzel:wght@700&family=Kaushan+Script&family=Oswald:wght@500&family=Open+Sans:wght@700&display=swap">
<style>
:root{
  --brand-blue:#2c3f97;
  --green-dark:#2f6d18;
  --green-mid:#5b9a2a;
  --lime:#c8d82a;
  --lime-light:#e6ef7a;
  --gold:#c9962e;
  --gold-light:#e2bb5a;
  --sky-light:#bfe6fb;
  --sky:#4fb5ec;
  --navy:#0f1f52;
  --corn:#3f6e2a;
  --wood:#b08f64;
  --wood-dark:#6e5234;
  --white:#ffffff;
  --ink:#1e2a24;
}
*{margin:0;padding:0;box-sizing:border-box}
html,body{width:1200px;height:762px;overflow:hidden;background:var(--white)}
.canvas{position:relative;width:1200px;height:762px}
.label{position:absolute;top:56px;width:502px;height:654px;overflow:hidden}
.label--wheat{left:76px}
.label--corn{left:631px}
.scene{position:absolute;inset:0}
.label--wheat .scene{background:linear-gradient(180deg,var(--lime) 0%,var(--lime-light) 18%,var(--green-mid) 42%,var(--gold-light) 58%,var(--gold) 100%)}
.label--corn .scene{background:
  radial-gradient(circle at 22% 62%,rgba(255,250,190,.95) 0,rgba(255,240,120,.5) 14%,rgba(255,240,120,0) 34%),
  linear-gradient(180deg,var(--sky) 0%,var(--sky-light) 20%,#3c7fc0 42%,var(--corn) 66%,var(--corn) 79%,var(--wood) 79%,var(--wood-dark) 100%)}
.side-bands{position:absolute;inset:0;width:100%;height:100%}
.brand{position:absolute;top:62px;left:0;width:100%;display:flex;justify-content:center;align-items:center;gap:10px}
.brand__mark{width:18px;height:18px;border-radius:50%;background:var(--brand-blue)}
.brand__name{font-family:"Cinzel",serif;font-weight:700;font-size:70px;color:var(--brand-blue);letter-spacing:1px;line-height:1}
.product{position:absolute;left:0;width:100%;text-align:center;font-family:"Kaushan Script",cursive;transform:rotate(-9deg);white-space:nowrap}
.product--sub{top:192px;font-size:56px;color:var(--white);-webkit-text-stroke:2px var(--ink);text-shadow:3px 3px 0 var(--ink)}
.product--main{top:270px;font-size:130px;line-height:1;color:var(--white);-webkit-text-stroke:3px var(--ink);text-shadow:4px 4px 0 var(--ink);left:-10px}
.product--fr{top:420px;font-size:50px;left:-16px}
.label--wheat .product--fr{color:#a8d25a;-webkit-text-stroke:2px var(--green-dark);text-shadow:2px 2px 0 var(--green-dark)}
.label--corn .product--fr{color:#bfe3fb;-webkit-text-stroke:2px var(--navy);text-shadow:2px 2px 0 var(--navy)}
.origin{position:absolute;left:12px;top:550px;font-family:"Open Sans",sans-serif;font-weight:700;font-size:13px;color:var(--ink);white-space:nowrap;text-shadow:0 0 2px var(--white),0 0 2px var(--white)}
.origin-box{position:absolute;left:12px;top:568px;width:154px;height:76px;background:var(--white)}
.pack{position:absolute;left:314px;top:540px;color:var(--white);white-space:nowrap}
.pack__weight{font-family:"Oswald",sans-serif;font-weight:500;font-size:24px;line-height:30px;text-shadow:0 0 2px var(--white)}
.label--wheat .pack__weight{color:var(--green-dark)}
.label--corn .pack__weight{color:var(--navy)}
.pack__weight b{font-size:29px;font-weight:500}
.pack__info{font-family:"Open Sans",sans-serif;font-weight:700;font-size:10.5px;line-height:12.4px;letter-spacing:-.1px;text-shadow:1px 1px 1px var(--ink),-1px 0 1px var(--ink)}
</style>
</head>
<body>
<div class="canvas">

  <section class="label label--wheat">
    <div class="scene" role="img" aria-label="Photo of a golden wheat field under a bright green sky"></div>
    <svg class="side-bands" viewBox="0 0 502 654" preserveAspectRatio="none" aria-hidden="true">
      <path d="M0 0 C40 120 30 330 0 470 Z" fill="var(--green-dark)"/>
      <path d="M502 0 C462 120 472 330 502 470 Z" fill="var(--green-dark)"/>
    </svg>
    <div class="brand"><span class="brand__mark"></span><span class="brand__name">KORVA</span></div>
    <p class="product product--sub">Self-Raising</p>
    <p class="product product--main">Flour</p>
    <p class="product product--fr">Farine Préparée</p>
    <p class="origin">PRODUCT OF CANADA</p>
    <div class="origin-box"></div>
    <div class="pack">
      <p class="pack__weight">NET WEIGHT <b>8LB</b></p>
      <p class="pack__info">PACKED BY:<br>KORVA SUPERMARKET INC.<br>1180 9 STREET NW<br>BRANDON, MB<br>T: (555) 014-2273<br>E: INFO@KORVA-MARKET.EXAMPLE</p>
    </div>
  </section>

  <section class="label label--corn">
    <div class="scene" role="img" aria-label="Photo of a sunlit corn field under a blue sky with a wooden table top in front"></div>
    <svg class="side-bands" viewBox="0 0 502 654" preserveAspectRatio="none" aria-hidden="true">
      <path d="M0 0 C40 120 30 330 0 470 Z" fill="var(--navy)" opacity=".85"/>
      <path d="M502 0 C462 120 472 330 502 470 Z" fill="var(--navy)" opacity=".85"/>
    </svg>
    <div class="brand"><span class="brand__mark"></span><span class="brand__name">KORVA</span></div>
    <p class="product product--sub">Self-Raising</p>
    <p class="product product--main">Flour</p>
    <p class="product product--fr">Farine Préparée</p>
    <p class="origin">PRODUCT OF CANADA</p>
    <div class="origin-box"></div>
    <div class="pack">
      <p class="pack__weight">NET WEIGHT <b>8LB</b></p>
      <p class="pack__info">PACKED BY:<br>KORVA SUPERMARKET INC.<br>1180 9 STREET NW<br>BRANDON, MB<br>T: (555) 014-2273<br>E: INFO@KORVA-MARKET.EXAMPLE</p>
    </div>
  </section>

</div>
</body>
</html>
```